Selvin: A Friday night in the Prophetic Flyer

We are holding 2 Friday night events, one on 10/25/19 and the other on 11/29/19.
The time frame is 6:30pm-9:00pm. These services will be a time of prayer/healing for the sick and will be prophetic as well. (There will be prophets prophesying over people)

The event is called: Selvin: A Friday night in the Prophetic
The flyer should also include the phrase/excerpt: "And they prophesied also".

Keywords/Phrases: Prophetic, Healing, Climbing in the Spirit, Higher level of Anointing...

Target Market(s)

those looking for healing, seeking a word from God

Colors

Designer to choose colors to be used in the design.

Requirements
Must have
• The event is called: Selvin: A Friday night in the Prophetic
• The flyer should also include the phrase/excerpt: "And they prophesied also".
• It must include the Tovik logo attached, either is fine, we have attached two different versions.
• It must have the dates, location, time
• Dates: October 25, 2019 and November 29, 2019
• Location: Hollard Community Center
• (Downtown Portland) 482 Wendle Street
• Portland, ME 04102
• Time: 6:30pm-9:00pm
• Contact Info: Tel. 207-555-3841
• email: contact@brimfield-hall.org
• web: www.tovik.org
Nice to have
• creativity in color scheme, the meaning of the word Selvin conveyed in a classy artistic way/design.
Should not have
• Crosses, pictures of churches

```html
<!DOCTYPE html>
<html lang="en">
<head>
<meta charset="utf-8">
<title>Selvin: A Friday night in the Prophetic</title>
<link rel="stylesheet" href="https://fonts.googleapis.com/css2?family=Playfair+Display:wght@400;700;900&family=Montserrat:wght@500;600;700&display=swap">
<style>
  :root {
    --navy: #14223d;
    --navy-soft: rgba(20, 34, 61, 0.92);
    --orange: #e8832a;
    --white: #ffffff;
    --mist-top: #6fb3a6;
    --mist-mid: #9cc7c6;
    --mist-low: #6f97b4;
    --mist-base: #4d7a9c;
  }
  * { box-sizing: border-box; margin: 0; padding: 0; }
  html, body { width: 863px; height: 1200px; overflow: hidden; background: var(--white); }
  .flyer {
    position: relative;
    width: 863px;
    height: 1200px;
    overflow: hidden;
    font-family: "Montserrat", sans-serif;
    color: var(--white);
  }
  .scenery {
    position: absolute; inset: 0;
    background: linear-gradient(180deg, var(--mist-top) 0%, #84bdb4 30%, var(--mist-mid) 48%, var(--mist-low) 72%, var(--mist-base) 100%);
  }
  .title-frame {
    position: absolute;
    left: 92px; top: 58px; width: 678px; height: 282px;
    border: 4px solid var(--navy);
    text-align: center;
  }
  .event-name {
    margin-top: 38px;
    font-family: "Playfair Display", serif;
    font-weight: 900;
    font-size: 124px;
    line-height: 1;
    letter-spacing: 4px;
    color: var(--navy);
  }
  .event-sub {
    display: block;
    margin: 20px 30px 0;
    background: var(--navy);
    font-weight: 600;
    font-size: 26px;
    letter-spacing: 1.5px;
    line-height: 44px;
  }
  .scripture {
    position: absolute;
    left: 0; right: 0; top: 286px;
    text-align: center;
    font-family: "Playfair Display", serif;
    font-size: 26px;
    letter-spacing: 1.5px;
    color: var(--white);
  }
  .details {
    position: absolute;
    left: 167px; top: 374px; width: 529px; height: 416px;
    background: var(--navy-soft);
    text-align: center;
    padding-top: 40px;
  }
  .venue {
    color: var(--orange);
    font-weight: 700;
    font-size: 31px;
    letter-spacing: 0.5px;
  }
  .address {
    margin-top: 8px;
    font-weight: 500;
    font-size: 20px;
    line-height: 28px;
    letter-spacing: 1px;
  }
  .dates {
    display: flex;
    justify-content: center;
    align-items: center;
    gap: 22px;
    margin-top: 36px;
    font-family: "Playfair Display", serif;
  }
  .date { font-size: 36px; line-height: 1.05; letter-spacing: 1px; }
  .date-day { display: block; }
  .amp { color: var(--orange); font-size: 92px; font-weight: 700; line-height: 1; }
  .time {
    display: inline-block;
    margin-top: 34px;
    padding: 10px 28px;
    border-top: 3px solid var(--white);
    border-bottom: 3px solid var(--white);
    font-weight: 600;
    font-size: 22px;
    letter-spacing: 1.5px;
  }
  .footer {
    position: absolute;
    left: 86px; top: 915px; width: 690px; height: 221px;
    background: var(--navy-soft);
    display: flex;
    align-items: center;
    justify-content: space-between;
    padding: 0 40px;
  }
  .org {
    display: flex; align-items: center; gap: 14px;
    font-family: "Playfair Display", serif;
    font-size: 62px;
    font-weight: 700;
    letter-spacing: 2px;
  }
  .org-dot { width: 22px; height: 22px; border-radius: 50%; background: var(--orange); }
  .contact {
    text-align: right;
    font-weight: 500;
    font-size: 21px;
    line-height: 36px;
    letter-spacing: 1px;
    text-transform: uppercase;
  }
</style>
</head>
<body>
  <main class="flyer">
    <div class="scenery" role="img" aria-label="Misty layered mountain ranges in teal and blue tones"></div>

    <header class="title-frame">
      <h1 class="event-name">SELVIN</h1>
      <span class="event-sub">A FRIDAY NIGHT IN THE PROPHETIC</span>
    </header>

    <p class="scripture">"AND THEY PROPHESIED ALSO"</p>

    <section class="details">
      <h2 class="venue">HOLLARD COMMUNITY CENTER</h2>
      <p class="address">DOWNTOWN PORTLAND<br>482 WENDLE ST. PORTLAND ME 04102</p>
      <div class="dates">
        <p class="date">OCTOBER<span class="date-day">25</span></p>
        <span class="amp">&amp;</span>
        <p class="date">NOVEMBER<span class="date-day">29</span></p>
      </div>
      <p class="date" style="font-family:'Playfair Display',serif;font-size:36px;margin-top:6px;">2019</p>
      <p class="time">6:30PM TO 9:00PM</p>
    </section>

    <footer class="footer">
      <div class="org"><span class="org-dot"></span>TOVIK</div>
      <div class="contact">
        <p>207-555-3841</p>
        <p>www.tovik.org</p>
        <p>contact@brimfield-hall.org</p>
      </div>
    </footer>
  </main>
</body>
</html>
```